The Lark Coffee Bags for Retail Sale

We need three retail coffee bags designed for The Lark Bourbon & Coffee.

I have included the spec sheet.

We would like it to match our menu- attached here.

Here is each bag:

#1. Text:
The Meridian Blend
Espresso
Central & South American
Considered their “Founder's” coffee, this popular blend is wonderful for both espresso and drip-brewed coffee. It is full-bodied and rich without bitterness. The flavor is broad and tangy, with great aromatic dimension.
Notes:
Ideally, we would like the outline of the ship in the same style as the building outline from our menu. We want the background of this bag in a jewel toned teal color and gold. I will include an example of the teal color.

#2. Text:
The Gangway Blend
Drip
French & Indonesian
Sweet, smoky, smooth and chocolaty. It begins with a French Roast, with its distinctive smoky qualities, and mellowed it with a chocolaty Vienna-roasted Indonesian for an eye-opening blend that offers the best of both worlds: a bold and subtle morning brew.
Note: This can use the same outline as the menu of the Halvorsen Building. We would like the background black on this bag.

#3. Text:
MARELLO DECAF Alpine Pure® Process
Earthy tones, smooth and sweet, mild acidity, and creamy texture.
This Alpine Pure® Process decaf is carefully roasted to bring out rich flavors. You'll find it hard to believe that you're drinking a decaffeinated coffee.

All bags must include the following information.

Roasted and Packaged by Quillayute Bean Roasters
Langley, WA 98311

NET WT 12oz (340g)

We also want all bags to have our logo and, on the back, the Quillayute Bean logo as they are the providers of the coffee.

Target Market(s)

Upscale Coffee Patrons

Industry/Entity Type

Coffee

Font styles to use
Serif

Requirements
Must have
• Correct colors, logo, blend name and tasting notes and legal retail notes
Nice to have
• Unique designs
Should not have
• anything outside the predescribed colors

```html
<!DOCTYPE html>
<html lang="en">
<head>
<meta charset="utf-8">
<title>The Lark Bourbon &amp; Coffee — The Meridian Blend Bag Front</title>
<link rel="stylesheet" href="https://fonts.googleapis.com/css2?family=Oswald:wght@400;500;600&family=Courier+Prime:wght@400;700&display=swap">
<style>
  :root {
    --canvas: #ffffff;
    --bag-teal: #0d4a50;
    --bag-teal-deep: #083539;
    --gold: #c99a45;
    --cream: #ece4c4;
    --rust: #a8401a;
    --ink: #2b2219;
  }
  * { box-sizing: border-box; margin: 0; padding: 0; }
  html, body { width: 1200px; height: 960px; overflow: hidden; background: var(--canvas); }
  .canvas { position: relative; width: 1200px; height: 960px; }

  .bag-front {
    position: absolute; left: 340px; top: 30px;
    width: 520px; height: 900px;
    background: linear-gradient(180deg, var(--bag-teal) 0%, var(--bag-teal-deep) 100%);
    overflow: hidden;
  }

  .blueprint-backdrop {
    position: absolute; left: 0; top: 0; width: 520px; height: 430px;
    background: linear-gradient(180deg, rgba(201,154,69,0.12), rgba(201,154,69,0.04) 80%, rgba(201,154,69,0));
  }

  .valve {
    position: absolute; left: 238px; top: 215px; width: 44px; height: 44px;
    border-radius: 50%; background: var(--bag-teal-deep);
    box-shadow: inset 0 0 0 1px rgba(0,0,0,0.35);
  }

  .brand {
    position: absolute; left: 0; top: 330px; width: 520px;
    text-align: center; color: var(--gold);
    font-family: "Oswald", sans-serif; font-weight: 500;
  }
  .brand-mark {
    display: block; width: 14px; height: 14px; margin: 0 auto 14px;
    background: var(--gold);
  }
  .brand-name { font-size: 52px; letter-spacing: 5px; line-height: 1; }
  .brand-tagline { font-size: 17px; letter-spacing: 3px; margin-top: 6px; }

  .stamp-label {
    position: absolute; left: 32px; top: 470px; width: 456px; height: 222px;
    padding: 7px;
    background: radial-gradient(circle at center, var(--cream) 4.5px, transparent 5px) -1px -1px / 12px 12px;
  }
  .stamp-face {
    width: 100%; height: 100%;
    background: var(--cream);
    padding: 10px 18px;
    color: var(--ink);
  }
  .blend-name {
    font-family: "Oswald", sans-serif; font-weight: 600;
    font-size: 36px; color: var(--rust); text-align: center;
    letter-spacing: 1px; line-height: 1.1;
    padding-bottom: 6px; border-bottom: 2px solid var(--ink);
  }
  .label-body { display: flex; margin-top: 8px; }
  .label-story {
    flex: 1; padding-right: 12px; border-right: 1.5px solid var(--ink);
    font-family: "Courier Prime", monospace; font-size: 9.5px;
    line-height: 1.3; text-transform: uppercase; text-align: center;
  }
  .net-weight {
    margin-top: 14px; text-align: left;
    font-size: 14px; letter-spacing: 0.5px; text-transform: uppercase;
  }
  .label-facts { width: 132px; padding-left: 12px; }
  .brew-method {
    font-family: "Oswald", sans-serif; font-weight: 500;
    font-size: 26px; color: var(--rust); text-align: center;
    padding: 10px 0 16px; border-bottom: 1.5px solid var(--ink);
  }
  .origin { display: flex; align-items: center; gap: 6px; margin-top: 10px; }
  .origin-map {
    width: 14px; height: 22px; flex: none;
    background: var(--rust); border-radius: 40% 60% 30% 50%;
  }
  .origin-text {
    font-family: "Courier Prime", monospace; font-size: 9.5px;
    text-transform: uppercase; line-height: 1.2;
  }

  .ship-illustration {
    position: absolute; left: 0; top: 720px; width: 300px; height: 180px;
    background: linear-gradient(160deg, rgba(201,154,69,0.55), rgba(201,154,69,0.25));
    clip-path: polygon(0 20%, 60% 0, 88% 0, 88% 40%, 100% 55%, 100% 100%, 0 100%);
  }

  .roaster-line {
    position: absolute; right: 24px; bottom: 28px; width: 180px;
    text-align: right; color: var(--gold);
    font-family: "Courier Prime", monospace; font-size: 10px;
    line-height: 1.4; text-transform: uppercase; letter-spacing: 0.5px;
  }
</style>
</head>
<body>
<main class="canvas">
  <section class="bag-front">
    <div class="blueprint-backdrop" role="img" aria-label="Faint architectural blueprint lines and measurements"></div>
    <div class="valve"></div>

    <header class="brand">
      <span class="brand-mark"></span>
      <div class="brand-name">THE LARK</div>
      <div class="brand-tagline">BOURBON &amp; COFFEE</div>
    </header>

    <div class="stamp-label">
      <div class="stamp-face">
        <h1 class="blend-name">THE MERIDIAN BLEND</h1>
        <div class="label-body">
          <div class="label-story">
            <p>Considered their “Founder’s” coffee, this popular blend is wonderful for both espresso and drip-brewed coffee. It is full-bodied and rich without bitterness. The flavor is broad and tangy, with great aromatic dimension.</p>
            <p class="net-weight">Net Wt 12 oz (340 g)</p>
          </div>
          <div class="label-facts">
            <div class="brew-method">ESPRESSO</div>
            <div class="origin">
              <span class="origin-map" role="img" aria-label="Small map of Central and South America"></span>
              <span class="origin-text">Central &amp;<br>South American</span>
            </div>
          </div>
        </div>
      </div>
    </div>

    <div class="ship-illustration" role="img" aria-label="Gold line drawing of a ship outline"></div>

    <p class="roaster-line">Roasted and packaged by<br>Quillayute Bean Roasters<br>Langley, WA 98311</p>
  </section>
</main>
</body>
</html>
```